120ml Jar Label — Masculine Cosmetic Foot Balm for Cracked, Hardworking Heels

We need a print-ready wraparound label for a 120ml jar — a brown/amber glass jar with a black metal screw lid (file photo attached).

--DO NOT PUT A BARCODE ON THE LABEL PLEASE--
**PLEASE READ "PLAN HUDDLE PROJECT BRIEF FINAL.MD" IN ATTACHED FILES IF YOU ARE SUBMITTING A DESIGN.**

The label is 190mm wide × 40mm high.
We need files to be in an .ai format with a 2mm bleed at the end.
Social media handle: @bramblekeepnz (facebook, instagram and tiktok)

Bramble Keep is a New Zealand foot-care brand making practical, no-nonsense products for hardworking men whose jobs wreck their feet. Our flagship product, Ridge Mender Balm, helps fix thick, cracked, hardworking skin.

Brand color scheme and overview is all in the brief file. You may add some brand aligned colors outside of the specified hex codes as you see fit to make a great design. Feel free to remove the "Bramble Keep" text from the logo so Bramble Keep is not doubled up on the front of the label

The tone we want: direct, rugged, and credible — like a workwear brand, not a spa brand. Most cracked-heel products on the market lean soft and feminine; we want to stand apart by looking like a serious fix for a real problem, made in New Zealand.

Full legal requirements for New Zealand cosmetic labelling (ingredients, directions, net contents, origin, etc.) are listed in the attached brief document — these are non-negotiable and must stay legible.

Please see the label attached "Label spacing guide" for this project's rough spacing guide. This label is the same size and sits well on the jar. This label doesn't need to be spaced quite as much as the Verin Label

I want to run the design for a week - I feel 7 days is a good amount of time for designers to see the work, digest the brief and create something remarkable and memorable for Bramble Keep.

Target Market(s)

Working men in New Zealand whose jobs or lifestyle put heavy wear on their feet — tradies, farmers, hospital/shift workers, hunters, and outdoors people. Practical, value-driven buyers rather than luxury skincare shoppers.

Industry/Entity Type

Beauty / Health & Wellness / Cosmetics

Font styles to use
Sans Serif
Other font styles liked:
• Montserrat (bold, headings), Inter (regular, body)

Colors
00AB8E
00BBA5
67D7C9
C6EFE9
E9F9F6
FFC000
F8CF3A
FAE287
FDF2CF
FEFAEE

Requirements
Must have
• All NZ cosmetic labelling requirements from the attached brief (product name, tag line, net contents, ingredients, directions, storage, made in NZ) — legible and complete, not omitted for aesthetics Fits 190mm × 40mm wraparound format for a 120ml brown jar with black lid Uses our existing brand colors: Deep Olive #3C4A34, Bone White #F4EFE6, Terracotta Clay #C1683D, and Warm Grey #4A4540 (exact palette in attached brief) Uses Montserrat (headings) and Inter (body) or close equivalents Incorporates our existing shield-and-wing logo (attached) Brand name and product name clearly readable from a normal shelf/bathroom-cabinet distance
Nice to have
• A style that could extend into a hero/product photo later, similar to the NZ-hills-backdrop look on our website (screenshot attached) — not required for the label itself, just good to keep in mind Original icon work (e.g. a small soak/apply/sock icon set) if it fits the rugged brand feel A design that could work as a small back-label/wraparound split if the front can't fit everything at a readable size
Should not have
• No pastel colors, floral motifs, or delicate script fonts — this should never look like spa/luxury skincare. Don't introduce new brand colors outside the palette provided other than black.

```html
<!DOCTYPE html>
<html lang="en">
<head>
<meta charset="utf-8">
<title>Bramble Keep – Ridge Mender Balm Label</title>
<link href="https://fonts.googleapis.com/css2?family=Montserrat:wght@500;600;700;800&display=swap" rel="stylesheet">
<style>
  :root {
    --forest: #1f3a2e;
    --teal: #0b8f84;
    --clay: #8a552b;
    --clay-light: #c8733a;
    --bone: #f4efe6;
    --ink: #14231c;
    --black: #0d0d0d;
    --silver-1: #ffffff;
    --silver-2: #d9d9d9;
    --silver-3: #9e9e9e;
  }
  * { box-sizing: border-box; margin: 0; padding: 0; }
  html, body { width: 1200px; height: 989px; overflow: hidden; background: #ffffff; }
  body { font-family: "Montserrat", sans-serif; position: relative; }

  .label {
    position: absolute; left: 80px; top: 367px;
    width: 1039px; height: 254px;
    background: var(--forest);
    overflow: hidden;
  }
  .panel { position: absolute; top: 0; height: 254px; }
  .panel--back { left: 0; width: 519px; }
  .panel--front { left: 519px; width: 520px; }

  .band-clay { position: absolute; left: 0; right: 0; top: 198px; height: 56px; background: var(--clay); }

  /* back panel */
  .info { position: absolute; left: 79px; top: 16px; width: 260px; color: var(--bone); font-size: 9.4px; line-height: 11.6px; font-weight: 500; }
  .info h3 { color: var(--clay-light); font-size: 9.4px; font-weight: 700; margin-left: -8px; }
  .info h3::before { content: "• "; }
  .info p { margin-bottom: 10px; }

  .mini-brand { position: absolute; left: 334px; top: 16px; width: 110px; }
  .mini-brand__row { display: flex; align-items: center; gap: 5px; }
  .mini-brand__dot { width: 22px; height: 22px; border-radius: 50%; background: var(--bone); flex: none; }
  .mini-brand__name { color: var(--bone); font-weight: 800; font-size: 14px; line-height: 14px; }
  .mini-brand__name small { font-size: 7px; }
  .mini-brand__product { color: var(--bone); font-size: 8.6px; font-weight: 700; margin-top: 4px; white-space: nowrap; }

  .footprints { position: absolute; left: 351px; top: 66px; width: 64px; height: 97px; background: linear-gradient(160deg, #ffffff, #e6e2da); border-radius: 30px 30px 24px 24px; }

  .for-man { position: absolute; left: 351px; top: 164px; color: var(--bone); font-weight: 800; line-height: 1; }
  .for-man span { display: block; font-size: 9px; font-weight: 700; }
  .for-man strong { display: block; font-size: 18px; margin-top: -2px; }

  .benefits { position: absolute; left: 0; top: 198px; height: 56px; width: 519px; }
  .benefit { position: absolute; top: 14px; display: flex; align-items: center; gap: 7px; color: var(--bone); }
  .benefit__icon { width: 28px; height: 28px; border-radius: 50%; background: var(--black); display: flex; align-items: center; justify-content: center; flex: none; }
  .benefit__text b { display: block; font-size: 12px; line-height: 12px; font-weight: 700; }
  .benefit__text span { display: block; font-size: 9px; line-height: 11px; font-weight: 500; }

  /* front panel */
  .tab { position: absolute; left: 144px; top: 0; width: 233px; height: 15px; background: var(--clay); border-radius: 0 0 6px 6px; }
  .brand-mark { position: absolute; left: 100px; top: 28px; width: 82px; height: 82px; border-radius: 50%; background: var(--bone); }
  .brand-name { position: absolute; left: 200px; top: 22px; color: #ffffff; font-weight: 800; font-size: 50px; line-height: 52px; letter-spacing: -0.5px; }
  .brand-name small { font-size: 24px; letter-spacing: 0; }
  .band-teal { position: absolute; left: 0; right: 0; top: 137px; height: 61px; background: var(--teal); text-align: center; color: var(--ink); }
  .product-name { font-size: 27px; font-weight: 800; margin-top: 9px; line-height: 30px; }
  .origin { font-size: 9px; font-weight: 700; margin-top: 1px; }
  .tagline { position: absolute; left: 90px; top: 208px; color: var(--bone); font-size: 12px; line-height: 17px; font-weight: 800; letter-spacing: 0.3px; }
  .netto { position: absolute; right: 0; top: 198px; width: 199px; height: 56px; background: linear-gradient(100deg, var(--silver-1) 0%, var(--silver-1) 40%, var(--silver-2) 65%, var(--silver-3) 80%, var(--silver-1) 100%); text-align: center; color: var(--black); }
  .netto span { display: block; font-size: 12px; font-weight: 600; margin-top: 9px; }
  .netto strong { display: block; font-size: 23px; font-weight: 700; line-height: 24px; }
</style>
</head>
<body>
<div class="label">
  <div class="band-clay"></div>

  <section class="panel panel--back">
    <div class="info">
      <h3>DIRECTIONS:</h3>
      <p>Gently massage a small amount onto face, body<br>and dry areas as required.</p>
      <h3>INGREDIENTS:</h3>
      <p>Shea Butter, Beef Tallow, Beeswax, Grape Seed Oil,<br>Vegetable Glycerin, Lanolin, Panthenol,<br>Gluconolactone, Sodium Benzoate, Allantoin,<br>Manuka Honey, Vitamin E, Tea Tree Essential Oil,<br>Lemon Myrtle Essential Oil, Rosemary Oleoresin Extract</p>
      <h3>STORAGE:</h3>
      <p>Keep out of direct sunlight, below 30°C. Best used<br>within six months of opening.</p>
    </div>

    <div class="mini-brand">
      <div class="mini-brand__row">
        <div class="mini-brand__dot"></div>
        <div class="mini-brand__name">Bramble<br>Keep<small>NZ</small></div>
      </div>
      <div class="mini-brand__product">Ridge Mender Balm</div>
    </div>

    <div class="footprints" role="img" aria-label="Pair of white bare footprints with small crack marks on the heels"></div>

    <div class="for-man"><span>FOR</span><strong>MAN</strong></div>

    <div class="benefits">
      <div class="benefit" style="left:97px">
        <div class="benefit__icon">
          <svg width="14" height="16" viewBox="0 0 14 16"><path d="M7 1 C4 6 2 8 2 10.5 A5 5 0 0 0 12 10.5 C12 8 10 6 7 1Z" fill="none" stroke="#fff" stroke-width="1.5"/></svg>
        </div>
        <div class="benefit__text"><b>Heals</b><span>Cracked Heels</span></div>
      </div>
      <div class="benefit" style="left:220px">
        <div class="benefit__icon">
          <svg width="18" height="18" viewBox="0 0 18 18" fill="none" stroke="#fff" stroke-width="1"><path d="M10 3 L11.5 8.5 L17 10 L11.5 11.5 L10 17 L8.5 11.5 L3 10 L8.5 8.5Z"/><path d="M4 1 L4.6 3.4 L7 4 L4.6 4.6 L4 7 L3.4 4.6 L1 4 L3.4 3.4Z"/></svg>
        </div>
        <div class="benefit__text"><b>Deep</b><span>Nourishment</span></div>
      </div>
      <div class="benefit" style="left:339px">
        <div class="benefit__icon">
          <svg width="16" height="16" viewBox="0 0 16 16" fill="none" stroke="#fff" stroke-width="1.3"><path d="M3 14 C3 7 7 3 14 2 C13 9 9 13 3 14Z"/><path d="M3 14 L10 6"/></svg>
        </div>
        <div class="benefit__text"><b>Soft and</b><b>Smooth</b></div>
      </div>
    </div>
  </section>

  <section class="panel panel--front">
    <div class="tab"></div>
    <div class="brand-mark"></div>
    <div class="brand-name">Bramble<br>Keep<small>NZ</small></div>
    <div class="band-teal">
      <div class="product-name">Ridge Mender Balm</div>
      <div class="origin">Made In New Zealand</div>
    </div>
    <div class="tagline">TREATS THICK, CRACKED,<br>HARDWORKING SKIN</div>
    <div class="netto"><span>Netto</span><strong>120ml</strong></div>
  </section>
</div>
</body>
</html>
```